BoltCrest Screw Box and Carton Design

We are BoltCrest, a new screw and nail supplier from Ireland. We need box designs branded for our new launch of screws and nails, Outer carton and inner individual boxes. We would like our branding to portray the image of a professional company. We have our logo attached which we would like to stand out so that people recognise the box if it were to be seen from a distance or in a shop.

Target Market(s)

Construction Industry

Industry/Entity Type

Construction

Contact Information for Business Card

Declan Murtagh
Owner
07482619037
declan@boltcrest.co.uk

Font styles to use
Sans Serif

Colors
3277b5

Requirements
Must have
• The Carton should be cost effective for the box maker. The carton will contain 10 boxes. If you could design them in such a way that they can be manipulated easily to cater for the various sizes. The internal boxes that hold the screws will have colour. I like the layout of the Korvex box where the lid folds out over the front of the box. Blue colour #009ee2 Grey colour #4a4a49
Nice to have
• I would like some upgraded design to the original BoltCrest box in the picture. I feel that this design does not cater well for labels or information to be placed on the box.

```html
<!DOCTYPE html>
<html lang="en">
<head>
<meta charset="utf-8">
<title>BoltCrest Mailer Box Dieline – 18 x 14 x 10 cm</title>
<link rel="stylesheet" href="https://fonts.googleapis.com/css2?family=Montserrat:wght@400;500;600;800&display=swap">
<style>
  :root {
    --brand-blue: #009ee2;
    --brand-grey: #4a4a49;
    --mid-grey: #525252;
    --dark-grey: #3d3d3c;
    --black: #000000;
    --white: #ffffff;
    --cut-line: #111111;
    --crease-line: #b0282e;
    --paper: #ffffff;
  }
  html, body {
    margin: 0;
    padding: 0;
    width: 1200px;
    height: 1200px;
    overflow: hidden;
    background: var(--paper);
  }
  .dieline {
    display: block;
    width: 1200px;
    height: 1200px;
    font-family: "Montserrat", sans-serif;
  }
  .fill-blue { fill: var(--brand-blue); }
  .fill-grey { fill: var(--brand-grey); }
  .fill-mid { fill: var(--mid-grey); }
  .fill-black { fill: var(--black); }
  .fill-white { fill: var(--white); }
  .cut { fill: none; stroke: var(--cut-line); stroke-width: 1; }
  .crease { fill: none; stroke: var(--crease-line); stroke-width: 0.8; }
  .rule { stroke: var(--white); stroke-width: 1.2; }
  .wordmark { font-weight: 800; }
  .wordmark--blue { fill: var(--brand-blue); }
  .wordmark--white { fill: var(--white); }
  .tagline { font-weight: 600; font-size: 8px; fill: var(--white); letter-spacing: 0.3px; }
  .contact { font-weight: 600; font-size: 8.5px; fill: var(--white); }
  .about { font-weight: 500; font-size: 8.4px; fill: var(--white); }
  .size-note { font-weight: 500; font-size: 15px; fill: var(--black); }
</style>
</head>
<body>
<svg class="dieline" viewBox="0 0 1300 1300" xmlns="http://www.w3.org/2000/svg" role="img" aria-label="BoltCrest mailer box flat dieline, 18 x 14 x 10 cm">
  <defs>
    <linearGradient id="panel-shade" x1="0" y1="0" x2="1" y2="1">
      <stop offset="0" stop-color="#000000"/>
      <stop offset="0.55" stop-color="#1c1c1c"/>
      <stop offset="1" stop-color="#474746"/>
    </linearGradient>
    <linearGradient id="flap-shade" x1="0" y1="0" x2="1" y2="0">
      <stop offset="0" stop-color="#4a4a49"/>
      <stop offset="1" stop-color="#009ee2"/>
    </linearGradient>
  </defs>

  <!-- Lid tuck flap -->
  <g class="lid-flap">
    <path class="fill-blue" d="M448 60 H830 C900 60 980 70 995 150 C1010 240 990 270 940 270 H360 C310 270 290 240 292 180 C296 70 390 60 448 60 Z"/>
    <rect x="448" y="60" width="382" height="202" fill="url(#flap-shade)" role="img" aria-label="Soft grey to blue backdrop for lid flap"/>
    <path class="cut" d="M448 72 H632 A18 18 0 0 0 668 72 H830 C890 72 968 80 982 155 C994 230 975 252 935 252 H365 C325 252 308 230 310 180 C314 85 390 72 448 72 Z"/>
    <line class="cut" x1="472" y1="62" x2="472" y2="262"/>
    <line class="cut" x1="828" y1="62" x2="828" y2="262"/>
    <g transform="rotate(180 650 165)">
      <line class="rule" x1="535" y1="177" x2="765" y2="177"/>
      <line class="rule" x1="535" y1="208" x2="765" y2="208"/>
      <text class="tagline" x="650" y="196" text-anchor="middle">● DRYLINING SUPPLIES ● FIXINGS ● TOOLS</text>
      <text class="wordmark wordmark--white" x="650" y="155" font-size="40" text-anchor="middle">BOLTCREST</text>
    </g>
  </g>

  <!-- Lid top panel with dust flaps -->
  <g class="lid-top">
    <path class="fill-blue" d="M412 282 H472 V548 H412 Z M830 282 H885 V548 H830 Z"/>
    <path class="fill-black" d="M428 285 L472 262 V548 L428 510 Z M830 262 L872 285 V510 L830 548 Z"/>
    <rect x="472" y="262" width="358" height="286" fill="url(#panel-shade)" role="img" aria-label="Dark gradient backdrop for lid top"/>
    <path class="cut" d="M428 285 L472 262 M428 285 V510 L472 548 M872 285 L830 262 M872 285 V510 L830 548"/>
    <rect class="crease" x="472" y="262" width="358" height="286"/>
    <text class="wordmark wordmark--white" transform="rotate(180 650 405)" x="650" y="422" font-size="46" text-anchor="middle">BOLTCREST</text>
  </g>

  <!-- Side walls -->
  <g class="side-walls">
    <path class="fill-blue" d="M215 338 H412 V548 H175 Z M885 338 H1085 L1125 548 H885 Z"/>
    <rect class="fill-blue" x="175" y="548" width="295" height="294"/>
    <rect class="fill-blue" x="830" y="548" width="295" height="294"/>
    <path class="cut" d="M222 348 H300 V340 H358 V348 H420 M190 540 L222 348 M880 348 H940 V340 H998 V348 H1078 L1112 540"/>
    <path class="cut" d="M190 758 V832 H462 V758 M838 758 V832 H1110 V758"/>
    <rect class="cut" x="300" y="755" width="60" height="4"/>
    <rect class="cut" x="940" y="755" width="60" height="4"/>
  </g>

  <!-- Brand band -->
  <g class="brand-band">
    <rect class="fill-white" x="175" y="548" width="950" height="45"/>
    <text class="wordmark wordmark--blue" x="445" y="582" font-size="26" text-anchor="end">BOLTCREST</text>
    <text class="wordmark wordmark--blue" x="808" y="582" font-size="26" text-anchor="end">BOLTCREST</text>
    <text class="wordmark wordmark--blue" x="1086" y="582" font-size="26" text-anchor="end">BOLTCREST</text>
  </g>

  <!-- Front panel -->
  <g class="front-panel">
    <rect x="470" y="593" width="360" height="155" fill="url(#panel-shade)" role="img" aria-label="Dark gradient backdrop for front panel"/>
    <text class="contact" x="490" y="709">www.boltcrest.co.uk</text>
    <text class="contact" x="490" y="728">e-mail: info@boltcrest.co.uk</text>
  </g>

  <!-- Information panels -->
  <g class="info-panels">
    <rect class="fill-white label-area" x="278" y="622" width="103" height="66" rx="3"/>
    <text class="about">
      <tspan x="862" y="656">BoltCrest is the platform to bring you the best</tspan>
      <tspan x="862" y="668">drylining tools and an excellent provider of</tspan>
      <tspan x="862" y="680">self-tapping screws in the UK.</tspan>
      <tspan x="862" y="692">Our equipment is meant to offer you comfort</tspan>
      <tspan x="862" y="704">and accuracy to enhance your work quality.</tspan>
    </text>
  </g>

  <!-- Grey stripe -->
  <g class="grey-stripe">
    <rect class="fill-mid" x="175" y="716" width="295" height="42"/>
    <rect class="fill-mid" x="830" y="716" width="295" height="42"/>
    <rect class="crease" x="175" y="548" width="950" height="200"/>
  </g>

  <!-- Base and back -->
  <g class="base">
    <rect class="fill-blue" x="458" y="748" width="382" height="282"/>
    <path class="cut" d="M462 758 L470 750 V1030 M838 758 L830 750 V1030"/>
    <rect class="fill-blue" x="210" y="1027" width="877" height="213"/>
    <rect class="cut" x="222" y="1037" width="855" height="193"/>
    <line class="crease" x1="474" y1="1030" x2="474" y2="1230"/>
    <line class="crease" x1="826" y1="1030" x2="826" y2="1230"/>
    <line class="crease" x1="470" y1="1030" x2="830" y2="1030"/>
  </g>

  <text class="size-note" x="275" y="973">18 x 14 x 10 cm</text>
</svg>
</body>
</html>
```